Marwood Holiday Jubilee 2025

We’re looking for a designer to help refresh the visual identity of our annual Christmas show while maintaining continuity from previous years. The updated design should feel festive, and warm, with a sense of celebration and anticipation. We’d like a central graphic that can be adapted for posters, social media, and digital signage, along with supporting assets for flyers and banners.

We’re open to seasonal color palettes such as rich reds, deep greens or blues, golds, silvers, or cool winter tones, and prefer typography that’s clear and elegant. The overall look should feel familiar to returning audiences while inviting and engaging for newcomers.

Two key groups: the current attenders of our congregation and the broader community in our suburb of Rochester, NY. Our congregation is made up of families, older adults, and young professionals who value faith, community and spiritual growth. The surrounding community is a fast growing friendly and family-oriented area of young professionals and longtime families.

We’re looking for a designer to help refresh the visual identity of our annual Christmas show while maintaining continuity with the theme and tone of previous years. The updated design should feel festive, and warm, with a sense of celebration and anticipation. We’d like a central graphic that can be adapted for posters, social media, and digital signage, along with supporting assets for flyers and banners.

Target Market(s)

Two key groups: the current attenders of our congregation and the broader community in our suburb of Rochester, NY. Our congregation is made up of families, older adults, and young professionals who value faith, community and spiritual growth. The surrounding community is a fast growing friendly and family-oriented area of young professionals and long time families.

Industry/Entity Type

Non-profit. Church

Font styles to use
Serif
Decorative
Script
Other font styles liked:
• Quentin

Requirements
Must have
• Sparkle, eye catching
Should not have
• must not look identical to the uploaded versions

```html
<!DOCTYPE html>
<html lang="en">
<head>
<meta charset="utf-8">
<title>Marwood Holiday Jubilee – Slide Concepts</title>
<link rel="stylesheet" href="https://fonts.googleapis.com/css2?family=Cinzel+Decorative:wght@400;700&family=Questrial&family=Mr+Dafoe&family=Josefin+Sans:ital,wght@0,600;0,700;1,600&display=swap">
<style>
  :root {
    --page: #ffffff;
    --night: #0b0806;
    --umber: #2a1606;
    --amber: #b8740f;
    --gold: #f2c24a;
    --gold-light: #ffe9a0;
    --spark: #fff4c8;
    --olive: #8c8a2c;
    --chartreuse: #a9b51c;
    --ember: #f07b25;
    --flame: #f25a1a;
    --silver: #c4c4cc;
    --silver-dim: #9c9ca6;
    --cocoa: #1e0e05;
  }
  * { margin: 0; padding: 0; box-sizing: border-box; }
  html, body { width: 1200px; height: 800px; overflow: hidden; background: var(--page); }
  .board { position: relative; width: 1200px; height: 800px; }

  .slide {
    position: absolute;
    left: 304px;
    width: 598px;
    height: 337px;
    overflow: hidden;
  }
  .slide--classic { top: 50px; }
  .slide--modern { top: 411px; }

  .glitter-backdrop {
    position: absolute; inset: 0;
    background:
      radial-gradient(ellipse 42% 50% at 76% 42%, rgba(242,194,74,.6), transparent 70%),
      radial-gradient(ellipse 85% 28% at 50% 100%, rgba(255,214,120,.95), rgba(200,130,20,.7) 55%, transparent 100%),
      radial-gradient(ellipse 55% 45% at 88% 18%, rgba(184,116,15,.5), transparent 70%),
      linear-gradient(100deg, var(--night) 0%, var(--umber) 42%, #5a3208 100%);
  }

  .sparkle-field {
    position: absolute; inset: 0;
    background:
      radial-gradient(circle at 6% 76%, var(--spark) 0 3px, transparent 6px),
      radial-gradient(circle at 11% 74%, var(--gold) 0 3px, transparent 6px),
      radial-gradient(circle at 16% 72%, var(--spark) 0 3px, transparent 6px),
      radial-gradient(circle at 4% 88%, var(--gold-light) 0 2px, transparent 5px),
      radial-gradient(circle at 10% 96%, var(--spark) 0 3px, transparent 6px),
      radial-gradient(circle at 30% 96%, var(--gold-light) 0 2px, transparent 5px),
      radial-gradient(circle at 50% 98%, var(--spark) 0 3px, transparent 7px),
      radial-gradient(circle at 62% 92%, var(--gold-light) 0 2px, transparent 5px),
      radial-gradient(circle at 73% 94%, var(--spark) 0 2px, transparent 5px),
      radial-gradient(circle at 88% 98%, var(--gold-light) 0 3px, transparent 6px),
      radial-gradient(circle at 96% 84%, var(--spark) 0 2px, transparent 5px),
      radial-gradient(circle at 88% 78%, var(--gold) 0 2px, transparent 5px),
      radial-gradient(circle at 12% 10%, var(--gold) 0 1.5px, transparent 3px),
      radial-gradient(circle at 22% 41%, var(--spark) 0 1.5px, transparent 3px),
      radial-gradient(circle at 12% 66%, var(--amber) 0 1.5px, transparent 3px),
      radial-gradient(circle at 23% 41%, var(--gold) 0 1.5px, transparent 3px),
      radial-gradient(circle at 33% 9%, var(--gold) 0 1.5px, transparent 3px),
      radial-gradient(circle at 53% 7%, var(--spark) 0 1.5px, transparent 3px),
      radial-gradient(circle at 70% 12%, var(--gold-light) 0 1.5px, transparent 3px),
      radial-gradient(circle at 78% 22%, var(--spark) 0 1.5px, transparent 3px),
      radial-gradient(circle at 84% 30%, var(--gold-light) 0 1.5px, transparent 3px),
      radial-gradient(circle at 92% 14%, var(--spark) 0 1.5px, transparent 3px),
      radial-gradient(circle at 74% 40%, var(--gold-light) 0 1.5px, transparent 3px),
      radial-gradient(circle at 86% 50%, var(--spark) 0 1.5px, transparent 3px),
      radial-gradient(circle at 95% 38%, var(--gold-light) 0 1.5px, transparent 3px),
      radial-gradient(circle at 80% 60%, var(--spark) 0 1.5px, transparent 3px),
      radial-gradient(circle at 67% 28%, var(--gold) 0 1px, transparent 2.5px),
      radial-gradient(circle at 98% 62%, var(--gold) 0 1px, transparent 2.5px);
  }

  .church-name {
    position: absolute; top: 54px; left: 50%; transform: translateX(-50%);
    white-space: nowrap;
    font-family: "Josefin Sans", sans-serif; font-weight: 700;
    font-size: 14px; letter-spacing: 1.6px;
    background: linear-gradient(90deg, var(--olive) 0%, var(--olive) 40%, var(--ember) 100%);
    -webkit-background-clip: text; background-clip: text; color: transparent;
  }
  .presents-rule {
    position: absolute; top: 75px; left: 190px; width: 218px; height: 1px;
    background: linear-gradient(90deg, var(--olive), var(--ember));
  }
  .presents {
    position: absolute; top: 68px; left: 50%; transform: translateX(-50%);
    padding: 0 3px;
    font-family: "Josefin Sans", sans-serif; font-style: italic; font-weight: 600;
    font-size: 12px; letter-spacing: .6px; color: var(--olive);
    background: #3b2208;
  }

  .title-glow {
    position: absolute; top: 190px; left: 120px; width: 360px; height: 80px;
    background: radial-gradient(ellipse at center, rgba(255,214,120,.85), rgba(230,160,50,.45) 50%, transparent 75%);
  }
  .title-swash {
    position: absolute; left: 50%; transform: translateX(-50%);
    white-space: nowrap; color: var(--chartreuse);
    font-family: "Cinzel Decorative", serif; font-weight: 700; line-height: 1;
  }
  .title-swash--first { top: 86px; font-size: 52px; }
  .title-swash--second { top: 144px; font-size: 56px; }
  .title-geometric {
    position: absolute; top: 204px; left: 50%; transform: translateX(-50%);
    font-family: "Questrial", sans-serif; font-size: 56px; line-height: 1;
    color: var(--cocoa); white-space: nowrap;
    text-shadow: 0 0 10px rgba(255,226,150,.7);
  }

  .date-rule {
    position: absolute; top: 259px; height: 1.5px;
    background: linear-gradient(90deg, transparent, var(--gold-light) 8%, var(--gold-light) 92%, transparent);
  }
  .slide--classic .date-rule { left: 117px; width: 376px; }
  .slide--modern .date-rule { left: 111px; width: 376px; }

  .date-band {
    position: absolute; top: 260px; left: 110px; width: 380px; height: 36px;
    background: radial-gradient(ellipse at center, rgba(40,22,10,.7), transparent 75%);
  }
  .event-date {
    position: absolute; top: 268px; left: 50%; transform: translateX(-50%);
    white-space: nowrap;
    font-family: "Josefin Sans", sans-serif; font-weight: 700;
    font-size: 22px; letter-spacing: 3.2px;
    background: linear-gradient(90deg, var(--ember) 0%, var(--flame) 42%, var(--silver) 62%, var(--silver-dim) 100%);
    -webkit-background-clip: text; background-clip: text; color: transparent;
  }
  .slide--modern .event-date { margin-left: -6px; }

  .title-spaced {
    position: absolute; left: 50%; transform: translateX(-50%);
    white-space: nowrap; line-height: 1;
    font-family: "Josefin Sans", sans-serif; font-weight: 600;
    background: linear-gradient(90deg, var(--ember) 0%, var(--chartreuse) 30%, var(--silver) 50%, var(--silver-dim) 100%);
    -webkit-background-clip: text; background-clip: text; color: transparent;
  }
  .title-spaced--first { top: 102px; font-size: 44px; letter-spacing: 24px; margin-left: 12px; }
  .title-spaced--second { top: 144px; font-size: 44px; letter-spacing: 22px; margin-left: 11px; }
  .title-script {
    position: absolute; top: 176px; left: 50%; transform: translateX(-50%);
    white-space: nowrap; line-height: 1.2;
    font-family: "Mr Dafoe", cursive; font-size: 84px; padding: 0 14px;
    background: linear-gradient(90deg, var(--ember) 0%, var(--flame) 45%, #f2d6c8 62%, var(--silver) 100%);
    -webkit-background-clip: text; background-clip: text; color: transparent;
  }
</style>
</head>
<body>
<main class="board">

  <section class="slide slide--classic" aria-label="Classic title slide">
    <div class="glitter-backdrop" role="img" aria-label="Golden glitter and bokeh sparkle background on dark brown">
      <div class="sparkle-field"></div>
    </div>
    <p class="church-name">CEDAR GROVE FELLOWSHIP CHURCH</p>
    <div class="presents-rule"></div>
    <p class="presents">presents</p>
    <div class="title-glow"></div>
    <h1 class="title-swash title-swash--first">Marwood</h1>
    <p class="title-swash title-swash--second">Holiday</p>
    <p class="title-geometric">Jubilee</p>
    <div class="date-rule"></div>
    <p class="event-date">DECEMBER 14 &amp; 15 6:00PM</p>
  </section>

  <section class="slide slide--modern" aria-label="Modern title slide">
    <div class="glitter-backdrop" role="img" aria-label="Golden glitter and bokeh sparkle background on dark brown">
      <div class="sparkle-field"></div>
    </div>
    <p class="church-name">CEDAR GROVE FELLOWSHIP CHURCH</p>
    <div class="presents-rule"></div>
    <p class="presents">presents</p>
    <h2 class="title-spaced title-spaced--first">MARWOOD</h2>
    <p class="title-spaced title-spaced--second">HOLIDAY</p>
    <p class="title-script">Jubilee</p>
    <div class="date-band"></div>
    <div class="date-rule"></div>
    <p class="event-date">DECEMBER 14 &amp; 15 6:00PM</p>
  </section>

</main>
</body>
</html>
```